Adult Literacy Program - flyer to attract volunteers and students

We want a flyer that is engaging, colorful, modern and will appeal to our primary audience of adults aged 40-60. We are trying to attract both prospective volunteers (typically age 50+, mostly women) and students (typically aged 40+).
The flyer should feature diverse people working together in pairs of two, reading or talking, with a workbook or some reading material in front of them.

Our organization trains tutors to work one-on-one with adults who are learning how to read. Most of our adult students are non-native speakers of English. Many are of Haitian or Hispanic origin, so we would like some people who represent that demographic.

The Flyer should represent reading, learning, literacy, knowledge, growth,
and opportunities.
Our students are learning to read so they can advance their job opportunities.

Target Market(s)

Adults aged 40-60, primarily women, retired, volunteers

Industry/Entity Type

Education

Font styles to use
Serif
Sans Serif

Colors

Designer to choose colors to be used in the design.

Requirements
Must have
• - UPDATE: Should be designed as a TRI-FOLD brochure on 8.5 x 11 inch paper that will be folded into thirds.
• - Images of diverse people, women and men, who look Hispanic, Haitian and other nationalities as well as Caucasian.
• - Our logo on the front cover
Nice to have
• The sample flyer is very boring and dry! We are open to different ways of presenting the text.

```html
<!DOCTYPE html>
<html lang="en">
<head>
<meta charset="UTF-8">
<title>Adult Literacy Program – Tri-fold Inside Spread</title>
<link href="https://fonts.googleapis.com/css2?family=Lato:wght@400;700;900&family=Montserrat:wght@700&display=swap" rel="stylesheet">
<style>
  :root {
    --teal: #2a9fba;
    --teal-box: #28a3be;
    --navy: #13235a;
    --ink: #1e1e24;
    --paper: #ffffff;
    --canvas: #e9e7e3;
    --photo-warm-a: #c9a26a;
    --photo-warm-b: #e8d2a8;
    --photo-red-a: #9c3a3a;
    --photo-red-b: #d8b9a0;
    --photo-blue-a: #5f83a8;
    --photo-blue-b: #cfd6d8;
    --photo-cover-a: #6f8fb8;
    --photo-cover-b: #c8463f;
  }
  * { box-sizing: border-box; margin: 0; padding: 0; }
  html, body { width: 1200px; height: 1200px; overflow: hidden; }
  body {
    background: var(--canvas);
    font-family: "Lato", "Gill Sans", sans-serif;
    color: var(--ink);
    position: relative;
  }
  .brochure {
    position: absolute;
    left: 30px; top: 160px;
    width: 1140px; height: 880px;
    display: flex;
    box-shadow: 0 4px 14px rgba(0,0,0,.25);
    background: var(--paper);
  }
  .panel {
    position: relative;
    width: 380px; height: 100%;
    background: var(--paper);
  }
  .panel--tutors { background: linear-gradient(to right, #fff 85%, #f1f1f1 100%); }
  .panel--students { background: linear-gradient(to right, #f4f4f4 0%, #fff 10%, #fff 90%, #f1f1f1 100%); border-left: 1px solid #e2e2e2; }
  .section-tag {
    position: absolute;
    left: 88px; top: 41px;
    width: 206px; height: 44px;
  }
  .section-tag svg { position: absolute; inset: 0; }
  .section-tag span {
    position: absolute; inset: 0;
    display: flex; align-items: center; justify-content: center;
    padding-right: 6px;
    font-family: "Montserrat", sans-serif;
    font-weight: 700; font-size: 23px; letter-spacing: 1px;
    color: #fff;
  }
  .points {
    position: absolute;
    left: 40px; top: 100px; width: 310px;
    list-style: none;
    font-size: 18.5px; line-height: 22.3px;
  }
  .points li { position: relative; padding-left: 23px; }
  .points li::before {
    content: "•"; position: absolute; left: 1px; top: 0;
  }
  .points .sub li { padding-left: 23px; }
  .tagline {
    position: absolute;
    left: 0; right: 0; top: 340px;
    text-align: center;
    font-weight: 900; font-size: 16px; line-height: 21px;
    color: var(--navy);
  }
  .photo {
    position: absolute;
    width: 298px; height: 204px;
  }
  .photo--top { top: 410px; }
  .photo--bottom { top: 634px; }
  .panel--tutors .photo { left: 41px; }
  .panel--students .photo { left: 40px; }
  .photo--warm { background: linear-gradient(135deg, var(--photo-warm-a), var(--photo-warm-b)); }
  .photo--red { background: linear-gradient(135deg, var(--photo-red-a), var(--photo-red-b)); }
  .photo--blue { background: linear-gradient(135deg, var(--photo-blue-a), var(--photo-blue-b)); }
  .panel--cover {
    background: linear-gradient(160deg, #4a5f7e 0%, var(--photo-cover-a) 35%, #a9bfd9 60%, var(--photo-cover-b) 85%);
  }
  .cover-slogan {
    position: absolute;
    left: 162px; top: 662px;
    width: 178px; height: 177px;
    background: var(--teal-box);
    color: #fff;
    font-size: 34px; line-height: 40px;
    padding: 30px 0 0 25px;
  }
</style>
</head>
<body>
  <div class="brochure">
    <section class="panel panel--tutors">
      <div class="section-tag">
        <svg viewBox="0 0 206 44" width="206" height="44">
          <polygon points="2,6 202,0 206,44 4,44" fill="var(--navy)"/>
          <polygon points="0,6 198,0 201,40 2,42" fill="var(--teal)"/>
        </svg>
        <span>TUTORS</span>
      </div>
      <ul class="points">
        <li>No special skills or degrees needed — just a degree of caring!</li>
        <li>Training offered throughout the year</li>
        <li>Tutors meet students weekly at a library</li>
        <li>Instructional materials provided</li>
        <li>Ongoing support available</li>
      </ul>
      <p class="tagline">Teach an adult to read<br>and you'll change a life forever.</p>
      <div class="photo photo--top photo--warm" role="img" aria-label="Photo of four diverse adults smiling around a library table"></div>
      <div class="photo photo--bottom photo--blue" role="img" aria-label="Photo of adults reading books together in a library"></div>
    </section>

    <section class="panel panel--students">
      <div class="section-tag">
        <svg viewBox="0 0 206 44" width="206" height="44">
          <polygon points="2,6 202,0 206,44 4,44" fill="var(--navy)"/>
          <polygon points="0,6 198,0 201,40 2,42" fill="var(--teal)"/>
        </svg>
        <span>STUDENTS</span>
      </div>
      <ul class="points">
        <li>Students are adults in need of
          <ul class="sub" style="list-style:none">
            <li>basic literacy skills</li>
            <li>pre-GED skills</li>
            <li>conversational English</li>
          </ul>
        </li>
        <li>Tutoring is free of charge</li>
        <li>Tutoring is one-on-one</li>
        <li>Flexible scheduling during library hours</li>
        <li>Lessons focus on student goals</li>
      </ul>
      <p class="tagline">If you can read,<br>you can tutor!</p>
      <div class="photo photo--top photo--red" role="img" aria-label="Photo of a diverse group of adults studying with books at a table"></div>
      <div class="photo photo--bottom photo--blue" role="img" aria-label="Photo of two women working together over a workbook in a library"></div>
    </section>

    <section class="panel panel--cover" role="img" aria-label="Photo of a tutor and an adult student reading a book together in a library">
      <div class="cover-slogan">Connect.<br>Inspire.<br>Enrich.</div>
    </section>
  </div>
</body>
</html>
```